Tidal Quill is a premium Spa and Salon only professional tanning brand.

We need a email template/newsletter that we can send to our client base any time we would like to share information with them.
Whether this is launching our Christmas gift, or sharing up and coming training dates it will be another avenue for us to stay in touch with our clients.
We like to think ourselves as the 'Verrington handbag' in the tanning world, Tidal Quill is a brand that is desirable and exclusive and has people hooked once they trial the brand and are blown away by the results.
www.tidal-quill-example.com

```html
<!DOCTYPE html>
<html lang="en">
<head>
<meta charset="utf-8">
<title>Tidal Quill — Newsletter</title>
<link rel="stylesheet" href="https://fonts.googleapis.com/css2?family=Raleway:wght@300;400;700&family=Questrial&display=swap">
<style>
:root{
  --ink:#1a1a1a;
  --white:#ffffff;
  --grey-text:#8a8a8a;
  --grey-band:#ececec;
  --grey-icon:#9a9a9a;
  --panel:#3b3b3b;
  --brand-brown:#7a3b2a;
  --gold:#f2c12e;
  --blue:#1e9fe0;
  --yellow:#f5d60a;
  --cyan:#12d6e2;
  --pink:#ff1b7c;
  --stockist:#c8875a;
  --link:#1e9fe0;
}
*{box-sizing:border-box;margin:0;padding:0}
html,body{width:1200px;height:3854px;overflow:hidden;background:var(--white)}
body{position:relative;font-family:"Questrial",Arial,sans-serif;color:var(--ink)}
.abs{position:absolute}

.hero-art{position:absolute;left:0;top:0;width:1200px;height:2500px}

.brand-mark{position:absolute;left:700px;top:34px;width:460px;text-align:right;
  font-family:"Raleway",sans-serif;font-weight:700;color:var(--brand-brown);
  font-size:84px;line-height:84px;letter-spacing:2px}

.tagline{position:absolute;left:733px;top:853px;width:467px;height:154px;background:var(--panel);
  padding:18px 0 0 30px;font-family:"Raleway",sans-serif}
.tagline .lead{display:block;color:var(--gold);font-size:46px;font-weight:400;line-height:54px}
.tagline .strong{display:block;color:var(--white);font-size:56px;font-weight:700;line-height:62px;letter-spacing:1px}

.product{position:absolute;width:555px;padding:0 24px 0 31px;color:var(--white)}
.product h2{font-family:"Raleway",sans-serif;font-weight:300;font-size:52px;line-height:58px}
.product .variant{font-size:25px;line-height:36px;margin-bottom:12px}
.product p{font-size:17.5px;line-height:27px}
.product .btn{display:inline-block;margin-top:20px;padding:0 18px;height:46px;line-height:46px;
  font-size:14px;font-weight:700;letter-spacing:.5px;color:var(--ink);font-family:"Raleway",sans-serif}
.is-blue h2{color:var(--blue)} .is-blue .btn{background:var(--blue)}
.is-yellow h2{color:var(--yellow)} .is-yellow .btn{background:var(--yellow)}
.is-cyan h2{color:var(--cyan)} .is-cyan .btn{background:var(--cyan)}
.is-pink h2{color:var(--pink)} .is-pink .btn{background:var(--pink)}

.signup-title{position:absolute;left:72px;top:2552px;font-family:"Raleway",sans-serif;font-size:48px;line-height:62px;color:var(--ink)}
.signup-title strong{display:block;font-weight:700}
.signup-form{position:absolute;left:535px;top:2580px;width:591px;height:78px;display:flex}
.signup-form .field{flex:1;border:2px solid var(--ink);font-size:24px;padding:0 28px;line-height:74px}
.signup-form .submit{width:154px;background:var(--ink);color:var(--white);font-family:"Raleway",sans-serif;
  font-weight:700;font-size:22px;text-align:center;line-height:78px}
.signup-note{position:absolute;left:72px;top:2716px;width:1050px;font-size:17.5px;line-height:32px;color:var(--grey-text)}
.unsubscribe{position:absolute;left:72px;top:2812px;font-size:20px;color:var(--link);text-decoration:underline}

.stockist{position:absolute;left:0;top:2917px;width:1200px;height:334px;background:var(--stockist)}
.stockist h3{position:absolute;left:0;width:1200px;top:60px;text-align:center;color:var(--white);
  font-family:"Raleway",sans-serif;font-weight:300;font-size:52px}
.stockist .rule{position:absolute;left:540px;top:131px;width:124px;height:5px;background:var(--white)}
.stockist .control{position:absolute;top:198px;height:77px;background:var(--white);font-size:23px;color:#a8a8a8;
  line-height:77px;padding:0 24px}
.stockist .control svg{position:absolute;right:26px;top:28px}

.details{position:absolute;top:3300px;font-size:18px;line-height:33px;color:var(--grey-text)}
.details h4{font-family:"Raleway",sans-serif;font-weight:400;font-size:36px;color:var(--ink);line-height:46px;margin-bottom:14px}
.details.address{right:642px;text-align:right}
.details.contact{left:648px}
.details a{color:var(--link);text-decoration:none}

.social{position:absolute;left:0;top:3534px;width:1200px;height:121px;background:var(--grey-band)}
.social svg{position:absolute;left:0;top:0}

.footer{position:absolute;left:0;top:3655px;width:1200px;height:199px;background:#000;
  text-align:center;padding-top:40px;font-family:"Raleway",sans-serif;font-weight:700;
  color:var(--white);font-size:58px;line-height:60px;letter-spacing:2px}
</style>
</head>
<body>

<svg class="hero-art" viewBox="0 0 1200 2500" xmlns="http://www.w3.org/2000/svg">
  <defs>
    <radialGradient id="heroTone" cx="0.3" cy="0.45" r="0.8">
      <stop offset="0" stop-color="#e3b08c"/>
      <stop offset="0.35" stop-color="#d9c3b2"/>
      <stop offset="1" stop-color="#f1eeec"/>
    </radialGradient>
    <linearGradient id="toneGradual" x1="0" y1="0" x2="1" y2="1">
      <stop offset="0" stop-color="#5a4a3e"/><stop offset="1" stop-color="#a88640"/>
    </linearGradient>
    <linearGradient id="toneMist" x1="0" y1="0" x2="1" y2="1">
      <stop offset="0" stop-color="#c89a22"/><stop offset="1" stop-color="#8a5a2e"/>
    </linearGradient>
    <linearGradient id="toneDark" x1="0" y1="0" x2="1" y2="1">
      <stop offset="0" stop-color="#d8d2cc"/><stop offset="1" stop-color="#7a5a48"/>
    </linearGradient>
    <linearGradient id="toneNew" x1="0" y1="0" x2="1" y2="1">
      <stop offset="0" stop-color="#8e8e8e"/><stop offset="1" stop-color="#3a3a3a"/>
    </linearGradient>
  </defs>

  <g role="img" aria-label="Photo: woman seen from behind, seated in a towel, with autumn leaves drifting across her back">
    <rect x="0" y="0" width="1200" height="1400" fill="url(#heroTone)"/>
  </g>
  <polygon points="0,1055 1200,1318 1200,2500 0,2500" fill="#ffffff"/>
  <line x1="0" y1="1080" x2="1200" y2="1343" stroke="#e2e2e2" stroke-width="3"/>

  <g role="img" aria-label="Photo: woman with long wavy hair in a mustard coat">
    <polygon points="31,1123 586,1234 586,1828 31,1717" fill="url(#toneGradual)"/>
  </g>
  <g role="img" aria-label="Photo: smiling woman in a red beret and colourful scarf in autumn light">
    <polygon points="617,1234 1172,1345 1172,1989 617,1878" fill="url(#toneMist)"/>
  </g>
  <g role="img" aria-label="Photo: woman with long dark hair in a loose white top">
    <polygon points="31,1787 586,1898 586,2490 31,2490" fill="url(#toneDark)"/>
  </g>
  <g role="img" aria-label="Photo: woman in a black beanie and sunglasses">
    <polygon points="617,1898 1172,2009 1172,2490 617,2490" fill="url(#toneNew)"/>
  </g>

  <rect x="31" y="1380" width="555" height="316" fill="#000" fill-opacity="0.45"/>
  <rect x="617" y="1483" width="555" height="317" fill="#000" fill-opacity="0.45"/>
  <rect x="31" y="2178" width="555" height="312" fill="#000" fill-opacity="0.45"/>
  <rect x="617" y="2178" width="555" height="312" fill="#000" fill-opacity="0.45"/>
</svg>

<div class="brand-mark">TIDAL<br>QUILL</div>

<div class="tagline">
  <span class="lead">A REVOLUTION IN</span>
  <span class="strong">SELF TANNING</span>
</div>

<section class="product is-blue" style="left:31px;top:1392px">
  <h2>Gradual Tan</h2>
  <div class="variant">Daily Lotion</div>
  <p>Much like our Gradual Tan, our Original and Dark formulas contain an organic formula that comes enriched with the same deep moisturisers.</p>
  <span class="btn">VIEW PRODUCT</span>
</section>

<section class="product is-yellow" style="left:617px;top:1496px">
  <h2>Tanning Mist</h2>
  <div class="variant">Orginal</div>
  <p>This organic formula is enriched with deep moisturisers and exotic botanical extracts that tone and firm the skin fighting cellulite whilst developing a naturally youthful, sunkissed glow.</p>
  <span class="btn">VIEW PRODUCT</span>
</section>

<section class="product is-cyan" style="left:31px;top:2192px">
  <h2>Tanning Mist</h2>
  <div class="variant">Dark</div>
  <p>For those with darker skin tones or this preference, these additional products provide the option of a richer darker colour.</p>
  <span class="btn">VIEW PRODUCT</span>
</section>

<section class="product is-pink" style="left:617px;top:2192px">
  <h2>New Bronze Mist</h2>
  <div class="variant">Orginal</div>
  <p>This organic formula is enriched with deep moisturisers and exotic botanical extracts that tone and firm the skin.</p>
  <span class="btn">VIEW PRODUCT</span>
</section>

<h3 class="signup-title">SIGN UP FOR OUR <strong>NEWSLETTER</strong></h3>
<div class="signup-form">
  <span class="field">Enter your Email</span>
  <span class="submit">SIGN UP!</span>
</div>
<p class="signup-note">Contrary to popular belief, Lorem Ipsum is not simply random text. It has roots in a piece of classical Latin literature from 45 BC, making it over 2000 years old.</p>
<a class="unsubscribe" href="#">Unsubscribe</a>

<section class="stockist">
  <h3>Find a stockist</h3>
  <span class="rule"></span>
  <div class="control" style="left:108px;width:478px">Select Country
    <svg width="24" height="20" viewBox="0 0 24 20"><polyline points="3,5 12,14 21,5" fill="none" stroke="#8a8a8a" stroke-width="3"/></svg>
  </div>
  <div class="control" style="left:617px;width:475px">Search...
    <svg width="22" height="22" viewBox="0 0 22 22"><circle cx="9" cy="9" r="6.5" fill="none" stroke="#8a8a8a" stroke-width="2.5"/><line x1="14" y1="14" x2="20" y2="20" stroke="#8a8a8a" stroke-width="2.5"/></svg>
  </div>
</section>

<div class="details address">
  <h4>Address</h4>
  Harrowfield Business Centre<br>
  Millbrook Lane Trade Park<br>
  Eastmere, County Wexley EM4 7QZ
</div>
<div class="details contact">
  <h4>Contact</h4>
  +00 (12) 345 678<br>
  +00 (12) 876 543<br>
  <a href="#">hello@tidal-quill-example.com</a>
</div>

<nav class="social" aria-label="Social links">
  <svg width="1200" height="121" viewBox="0 0 1200 121">
    <circle cx="463" cy="64" r="14" fill="var(--grey-icon)"/>
    <circle cx="524" cy="64" r="14" fill="var(--grey-icon)"/>
    <circle cx="596" cy="64" r="14" fill="var(--grey-icon)"/>
    <circle cx="668" cy="64" r="14" fill="var(--grey-icon)"/>
    <circle cx="735" cy="64" r="14" fill="var(--grey-icon)"/>
  </svg>
</nav>

<footer class="footer">TIDAL<br>QUILL</footer>

</body>
</html>
```